Plumbing & Heating bussiness card design

i do all plumbing and heating work and need a catchy design. keep it simple but eye catching nothing gimicky
i do 24hr call outs
landlord safety checks
all aspects of plumbing and heating
boiler breakdowns
Flue sure reg number 804617
i have put up my old card. not to bothered about the front but i have put up the back for the details. mobile number and office are the same and the email has changed to tolwenpipes@mailvoro.net

Industry/Entity Type

Safety

Contact Information for Business Card

i do 24hr call outs
landlord safety checks
boiler breakdowns

Requirements
Must have
• i do 24hr call outs
• landlord safety checks
• all aspects of plumbing and heating
• boiler breakdowns
• Flue sure reg number 804617

```html
<!DOCTYPE html>
<html lang="en">
<head>
<meta charset="utf-8">
<title>Tolwen Plumbing &amp; Heating – Business Card</title>
<link href="https://fonts.googleapis.com/css2?family=Source+Sans+3:wght@400;600;700&display=swap" rel="stylesheet">
<style>
  :root {
    --backdrop-top: #2a2a2a;
    --backdrop-bottom: #050505;
    --card: #ffffff;
    --brand-red: #b5121b;
    --brand-blue: #1f6fb8;
    --icon-blue: #2a8fd6;
    --charcoal: #3a3d42;
  }
  * { margin: 0; padding: 0; box-sizing: border-box; }
  html, body { width: 1200px; height: 900px; overflow: hidden; }
  body {
    background: linear-gradient(180deg, var(--backdrop-top) 0%, #1a1a1a 45%, var(--backdrop-bottom) 100%);
    font-family: "Source Sans 3", "Myriad Pro", Arial, sans-serif;
    position: relative;
  }
  .card {
    position: absolute;
    top: 306px;
    width: 440px;
    height: 271px;
    background: var(--card);
    border-radius: 12px;
  }
  .card--front { left: 149px; width: 439px; }
  .card--back { left: 608px; width: 441px; height: 272px; }

  .wordmark {
    position: absolute;
    color: var(--charcoal);
    font-weight: 700;
    line-height: 1.05;
    text-align: center;
  }
  .card--front .wordmark { left: 14px; top: 100px; width: 204px; }
  .wordmark__main { display: block; font-size: 31px; letter-spacing: 0.5px; }
  .wordmark__sub { display: block; font-size: 15.5px; letter-spacing: 0.4px; margin-top: 4px; }
  .card--back .wordmark { left: 19px; top: 112px; width: 166px; }
  .card--back .wordmark__main { font-size: 28px; }
  .card--back .wordmark__sub { font-size: 12.5px; }

  .contact { position: absolute; left: 233px; top: 40px; color: var(--brand-red); }
  .contact__name { font-size: 19px; font-weight: 700; line-height: 1; }
  .contact__name .first { color: var(--brand-blue); }
  .contact__role { font-size: 13px; margin-top: 5px; }
  .contact__address { font-size: 13px; line-height: 15px; margin-top: 18px; }
  .contact__lines { list-style: none; margin-top: 13px; font-size: 13px; line-height: 16px; }
  .contact__lines li { display: flex; align-items: center; }
  .contact__lines svg { width: 9px; height: 9px; margin: 0 10px 0 3px; fill: var(--icon-blue); flex: none; }

  .services {
    position: absolute; left: 202px; top: 90px;
    list-style: none; color: var(--brand-red);
    font-size: 13px; font-weight: 700; line-height: 18.2px;
  }
  .services li { display: flex; align-items: center; }
  .services li::before {
    content: ""; width: 6px; height: 6px; border-radius: 50%;
    background: var(--icon-blue); margin-right: 7px; flex: none;
  }
</style>
</head>
<body>
  <section class="card card--front" aria-label="Business card front">
    <div class="wordmark">
      <span class="wordmark__main">TOLWEN</span>
      <span class="wordmark__sub">PLUMBING &amp; HEATING</span>
    </div>
    <div class="contact">
      <p class="contact__name"><span class="first">Owen</span> Tallis</p>
      <p class="contact__role">Managing Director</p>
      <p class="contact__address">1234, Address Goes Here<br>Country Name, 123456</p>
      <ul class="contact__lines">
        <li><svg viewBox="0 0 10 10"><rect x="2.5" y="0" width="5" height="10" rx="1"/></svg>123-456-7890</li>
        <li><svg viewBox="0 0 10 10"><path d="M0 3 Q5 0 10 3 V5 H7 V4 H3 V5 H0Z M2 6 H8 L9 10 H1Z"/></svg>123-456-7890</li>
        <li><svg viewBox="0 0 10 10"><rect x="1" y="3" width="8" height="7" rx="1"/><rect x="3" y="0" width="4" height="3"/></svg>123-456-7890</li>
        <li><svg viewBox="0 0 10 10"><path d="M0 2 H10 V8 H0Z M0 2 L5 6 L10 2" /></svg>info@youremail.com</li>
        <li><svg viewBox="0 0 10 10"><path d="M1 7 L6 2 A2 2 0 0 1 8 4 L3 9 A1.5 1.5 0 0 1 1 7Z"/></svg>www.yourweb.com</li>
      </ul>
    </div>
  </section>

  <section class="card card--back" aria-label="Business card back">
    <div class="wordmark">
      <span class="wordmark__main">TOLWEN</span>
      <span class="wordmark__sub">PLUMBING &amp; HEATING</span>
    </div>
    <ul class="services">
      <li>I do 24hr call outs</li>
      <li>Landlord safety checks</li>
      <li>All aspects of plumbing and heating</li>
      <li>Boiler breakdowns</li>
      <li>Flue sure reg number 804617</li>
    </ul>
  </section>
</body>
</html>
```